Art Wall - Illustrates "Be Colorful"

I have a seasonal color business called Willow Gate Blooms. We plant containers and add colorful annuals to garden beds. I need a 6' tall by 18' long banner that will be hung on a wall or possibly used on the side of my enclosed trailer. The banner will be used as backdrop for ladies taking pictures together and as a backdrop for colorful container gardens to be photographed for our website. It should have the words "Be Colorful" on it. I would like for it to look like a fun art wall that you would take a picture in front of in a downtown area. The art should work well with our logo. We love flowers but other ideas are welcome. Feel free to look at our instagram @willowgatebloomsokc to see examples of our work. I have uploaded our logo and a colorful flower picture we liked (great colors) but didn't quite work with our logo and a fun colorful wall at a restaurant that we really like.

Target Market(s)

women ages 30-45, wealthy, like to feel like they are trendy

Industry/Entity Type

Landscape Gardening

Font styles to use
Serif

Requirements
Must have
• The words "Be Colorful" on it and some space that would good for people to stand or objects to be placed to be photographed.
Nice to have
• We really like the colors in the "sun and skip" t-shirt picture I have attached. Also like the watercolor, alcohol ink, or hand-painted look.
Should not have
• Please do not include our logo on the banner. It will be added as a watermark to our photos.

Please do not literally use the logo flower in the design. Feel free to use pieces or inspiration from the logo but the wall should look more like art and less like a cartoon.

```html
<!DOCTYPE html>
<html lang="en">
<head>
<meta charset="utf-8">
<title>Be Colorful — Art Wall Banner</title>
<link rel="stylesheet" href="https://fonts.googleapis.com/css2?family=Noto+Serif:wght@700&display=swap">
<style>
  :root {
    --paint-orange: #ff6a00;
    --paint-sky: #84d4f4;
    --paint-violet: #9a5ed8;
    --paint-teal: #0b8a7c;
    --paint-yellow: #fbd800;
    --paint-amber: #ff8a00;
    --wall-white: #ffffff;
    --headline: #ffffff;
  }
  html, body {
    margin: 0;
    padding: 0;
    overflow: hidden;
    background: var(--wall-white);
  }
  .banner {
    position: relative;
    width: 1200px;
    height: 400px;
    overflow: hidden;
    background: var(--wall-white);
  }
  .paint-drips {
    position: absolute;
    inset: 0;
    background:
      linear-gradient(to bottom,
        rgba(255,255,255,0) 0%,
        rgba(255,255,255,0) 58%,
        rgba(255,255,255,0.75) 80%,
        var(--wall-white) 100%),
      linear-gradient(to right,
        var(--paint-orange) 0%,
        var(--paint-orange) 6%,
        var(--paint-teal) 8%,
        var(--paint-sky) 11%,
        var(--paint-sky) 19%,
        var(--paint-yellow) 21%,
        var(--paint-violet) 25%,
        var(--paint-violet) 32%,
        var(--paint-teal) 36%,
        var(--paint-teal) 42%,
        var(--paint-yellow) 46%,
        var(--paint-amber) 51%,
        var(--paint-amber) 59%,
        var(--paint-yellow) 64%,
        var(--paint-teal) 70%,
        var(--paint-teal) 76%,
        var(--paint-violet) 82%,
        var(--paint-violet) 88%,
        var(--paint-yellow) 91%,
        var(--paint-sky) 94%,
        var(--paint-sky) 100%);
  }
  .headline {
    position: absolute;
    top: 18px;
    right: 30px;
    margin: 0;
    font-family: "Noto Serif", Georgia, serif;
    font-weight: 700;
    font-size: 76px;
    line-height: 1;
    letter-spacing: 0.5px;
    color: var(--headline);
    text-transform: uppercase;
    white-space: nowrap;
    text-shadow: 0 0 14px rgba(0,0,0,0.18);
  }
</style>
</head>
<body>
  <main class="banner">
    <div class="paint-drips" role="img" aria-label="Bands of orange, sky blue, violet, teal and yellow paint dripping down onto a white wall"></div>
    <h1 class="headline">Be Colorful</h1>
  </main>
</body>
</html>
```